"Tidelark Ministry" needs a logo design that represents a Christian family boating ministry

Mission Statement:
“Providing compassion, care and opportunities to create memories for marginalized groups of society through ocean therapy.”
Bible verse:
Colossians 3:12 – “Therefore, as God’s chosen people, holy and dearly loved, clothe yourselves with compassion, kindness, humility, gentleness and patience.”
Target Market(s)
HOMELESS (who have gone through shelters and are on the road to recovery)
CHURCH GROUPS
INJURED MILITARY VETERANS
YOUTH AT RISK (orphans, human trafficking survivors)
SICKLY (hospitalized who can get out once in a while)
CAREGIVERS (single moms, military spouses caring for injured vets, families of those in prison)
ELDERLY (retirement centers)
SMALL BUSINESS STAFF OUTINGS
SPECIAL EVENTS
Industry/Entity Type
Ministry
Contact Information for Business Card
Captain Glen Marbury @ 555-014-2931
Priscilla Marbury @ 555-018-6457
info@tidelarkministry-example.com
www.tidelarkministry-example.com (not active yet but hopefully, soon)
Requirements
Must have
- Catch-phrase words maybe for back of business card:
- "Tidelark --- Kindness --- Sharing days on the waves"
Nice to have
- Added 2 photo files just for visuals:
- 1 photo is of our boat.
- Other photo is our daughter's artwork on a cooler she made (for father's day gift)...might be nice and fun to incorporate daughter's artwork/inspiration into logo...but not sure if it looks to busy

```html
<!DOCTYPE html>
<html lang="en">
<head>
<meta charset="utf-8">
<title>Tidelark Ministry – Business Card</title>
<link rel="stylesheet" href="https://fonts.googleapis.com/css2?family=Audiowide&display=swap">
<style>
  :root {
    --backdrop: #e9e9eb;
    --fold: #d4d5d8;
    --card: #ffffff;
    --navy: #2a2f3b;
    --sky: #03a9e8;
    --sky-deep: #0386c0;
    --ink: #2a2f3b;
    --paper-text: #ffffff;
  }
  html, body {
    margin: 0;
    padding: 0;
    width: 1200px;
    height: 1000px;
    overflow: hidden;
    background: var(--backdrop);
  }
  .sheet { display: block; width: 1200px; height: 1000px; }
  .fold { fill: var(--fold); }
  .card-face { fill: var(--card); }
  .panel { fill: var(--navy); }
  .tile { fill: var(--sky); }
  .tile-edge { fill: var(--sky-deep); }
  .icon { fill: none; stroke: #ffffff; stroke-width: 2; }
  .icon-solid { fill: #ffffff; }
  .name, .tagline {
    font-family: "Audiowide", sans-serif;
    fill: var(--paper-text);
  }
  .name { font-size: 21px; letter-spacing: 1.5px; }
  .tagline { font-size: 15px; letter-spacing: 1.2px; }
  .contact {
    font-family: "Audiowide", sans-serif;
    fill: var(--ink);
    font-size: 13px;
    letter-spacing: 1.5px;
  }
  .contact-web { font-size: 11px; letter-spacing: 1px; }
  .wordmark {
    font-family: "Audiowide", sans-serif;
    fill: var(--ink);
    font-size: 19px;
    letter-spacing: 1px;
  }
</style>
</head>
<body>
<svg class="sheet" viewBox="0 0 1200 1000" xmlns="http://www.w3.org/2000/svg">
  <defs>
    <linearGradient id="boat-tone" x1="0" y1="0" x2="0" y2="1">
      <stop offset="0" stop-color="#dff1f7"/>
      <stop offset="1" stop-color="#5bbcd6"/>
    </linearGradient>
  </defs>

  <!-- Front of card -->
  <g class="card card-front">
    <polygon class="fold" points="242,422 298,422 298,478"/>
    <rect class="card-face" x="298" y="117" width="632" height="361"/>
    <polygon class="panel" points="298,117 655,117 420,478 298,478"/>
    <polygon class="panel" points="665,117 725,117 683,183 623,183"/>
    <polygon class="panel" points="470,418 530,418 492,478 432,478"/>
    <polygon class="panel" points="623,183 631,183 478,418 470,418"/>

    <g class="contact-tile">
      <polygon class="tile-edge" points="612,199 672,199 636,256 632,256 662,205 612,205"/>
      <polygon class="tile" points="612,199 668,199 632,256 577,256"/>
      <g transform="translate(623,228)">
        <path class="icon-solid" d="M-11,-5 q11,-8 22,0 l-1,4 h-5 v-3 h-10 v3 h-5z"/>
        <rect class="icon-solid" x="-8" y="-1" width="16" height="11" rx="2"/>
        <circle cx="0" cy="4" r="3" fill="var(--sky)"/>
      </g>
    </g>

    <g class="contact-tile">
      <polygon class="tile" points="565,271 625,271 589,332 529,332"/>
      <g transform="translate(577,300)">
        <path class="icon-solid" d="M0,16 C-6,7 -10,2 -10,-4 A10,10 0 0 1 10,-4 C10,2 6,7 0,16z"/>
        <circle cx="0" cy="-4" r="4" fill="var(--sky)"/>
      </g>
    </g>

    <g class="contact-tile">
      <polygon class="tile" points="533,345 578,345 543,404 482,404"/>
      <g transform="translate(531,374)">
        <circle class="icon" r="12"/>
        <ellipse class="icon" rx="5" ry="12"/>
        <line class="icon" x1="-12" y1="0" x2="12" y2="0"/>
        <line class="icon" x1="-10" y1="-6" x2="10" y2="-6"/>
        <line class="icon" x1="-10" y1="6" x2="10" y2="6"/>
      </g>
    </g>

    <g class="names">
      <text class="name" x="320" y="165">CAPTAIN GLEN</text>
      <text class="name" x="416" y="192">&amp;</text>
      <text class="name" x="352" y="216">PRISCILLA</text>
      <text class="name" x="349" y="254" style="font-size:19px">MARBURY</text>
    </g>

    <g class="contacts">
      <text class="contact" x="683" y="222">555-018-6457</text>
      <text class="contact" x="673" y="245">555-014-2931</text>
      <text class="contact contact-web" x="625" y="303">WWW.TIDELARKMINISTRY-EXAMPLE.COM</text>
      <text class="contact contact-web" x="590" y="380">INFO@TIDELARKMINISTRY-EXAMPLE.COM</text>
    </g>
  </g>

  <!-- Back of card -->
  <g class="card card-back">
    <polygon class="fold" points="243,828 299,828 299,884"/>
    <rect class="card-face" x="299" y="522" width="633" height="362"/>
    <polygon class="panel" points="299,522 655,522 424,884 299,884"/>
    <polygon class="panel" points="667,522 727,522 494,884 434,884"/>

    <g class="taglines">
      <text class="tagline" x="311" y="572">TIDELARK</text>
      <text class="tagline" x="311" y="642">KINDNESS</text>
      <text class="tagline" x="311" y="709">SHARING DAYS</text>
      <text class="tagline" x="311" y="732">ON THE WAVES</text>
    </g>

    <rect class="boat-art" x="643" y="645" width="257" height="135" rx="6" fill="url(#boat-tone)"
          role="img" aria-label="Illustration of a family aboard a sport-fishing boat with a cross on its mast"/>

    <text class="wordmark" x="770" y="813" text-anchor="middle">TIDELARK MINISTRY</text>
  </g>
</svg>
</body>
</html>
```